Web portal for events

The project is about creating a web application - portal for culture events in Denmark.

Design

We aim for very simplistic, light and fully responsive design. The white background is preferable, as well as light color tones. As inspirational points we like the colors used in www.brimvale.com and www.tallowpine.org

FORMAT AND REQUIREMENTS:
1. Design should be provided based on the wireframes specified as a link below.
2. The design (and all of its pages) should be provided in three resolution variants:
- Desktop
- Tablet
- Phone
3. The design should be provided as PSD, where each page/section should be in its own PSD file
4. All graphical elements in the design should be delivered as single layers which can then be extracted from the PSD.
5. All graphical elements (icons, graphical buttons, etc.) should be provided as vector objects in the PSD, so that they can be exported into different sizes without loss of quality (for responsiveness)
6. The design should use either web safe fonts or Google Fonts.

RESPONSIVENESS
The web application should be visible on any devices (i.e. responsive design)

WIREFRAMES:
https://quillmarsh.examplewire.com/projects/eventloom/prototype/Homepage?key=0000000000000000000000000000000000000000

We expect design of the following wireframes:

Homepage:
https://quillmarsh.examplewire.com/projects/eventloom/Homepage

For arrangører - billede uploaded:
https://quillmarsh.examplewire.com/projects/eventloom/For%20arrang%C3%B8rer%20-%20billede%20uploaded

Further specifications of the project (i.e. functionality, etc.):
https://files.dorvexa.com/document/d/0AbCdEfGhIjKlMnOpQrStUvWxYz0123456789abcdefg/edit?usp=sharing
Updates

```html
<!DOCTYPE html>
<html lang="da">
<head>
<meta charset="utf-8">
<title>KULTRO – Din Guide til kultur og events</title>
<link href="https://fonts.googleapis.com/css2?family=Lato:wght@400;700&family=Montserrat:wght@600;700&family=Kaushan+Script&display=swap" rel="stylesheet">
<style>
:root{
  --brand:#ff3c10;
  --brand-dark:#e2380f;
  --ink-dark:#2b0a04;
  --cta:#e31212;
  --accent:#f04a24;
  --nav-bg:#efefef;
  --text:#222;
  --muted:#777;
  --line:#d8d8d8;
}
*{box-sizing:border-box;margin:0;padding:0}
html,body{width:983px;height:1200px;overflow:hidden;background:#fff}
body{position:relative;font-family:'Lato',sans-serif;color:var(--text)}
.abs{position:absolute}

/* header */
.site-header{position:absolute;left:0;top:0;width:983px;height:74px;background:var(--brand)}
.brand{position:absolute;left:147px;top:0;width:139px;height:72px;background:var(--brand-dark);padding:16px 0 0 7px;color:#fff}
.brand-name{font-family:'Montserrat',sans-serif;font-weight:700;font-size:17px;letter-spacing:.5px;line-height:18px}
.brand-tag{font-family:'Montserrat',sans-serif;font-weight:600;font-size:7.8px;margin-top:4px}
.search{position:absolute;left:296px;top:23px;width:364px;height:28px;background:#fff;border-radius:14px;border:2px solid #ffb9a5;display:flex;align-items:center;padding-left:12px;font-size:10px;color:#999}
.search svg{margin-right:6px}
.btn-dark{position:absolute;background:var(--ink-dark);color:#fff;font-size:10.5px;display:flex;align-items:center;justify-content:center}
.btn-search{left:668px;top:26px;width:45px;height:25px;font-family:'Montserrat',sans-serif;font-weight:600}
.btn-advanced{left:724px;top:26px;width:112px;height:25px;font-family:'Montserrat',sans-serif;font-weight:600}
.btn-login{left:894px;top:0;width:72px;height:26px;font-size:9.5px}

/* category nav */
.category-nav{position:absolute;left:0;top:74px;width:983px;height:48px;background:var(--nav-bg);border-bottom:1px solid var(--line)}
.category-nav ul{list-style:none;display:flex;position:absolute;left:147px;top:19px;font-size:10.5px}
.category-nav li{margin-right:30px;line-height:17px}
.category-nav li.active{background:#1c1c1c;color:#fff;border-radius:9px;padding:0 8px;margin-right:22px}

/* hero */
.hero{position:absolute;left:147px;top:133px;width:689px;height:257px;background:linear-gradient(100deg,#3a1a10 0%,#7a3a18 30%,#c5621c 55%,#e59a3a 70%,#8a3c12 100%)}
.hero-title{position:absolute;left:391px;top:68px;font-family:'Kaushan Script',cursive;color:#fff;font-size:35px}
.hero-text{position:absolute;left:400px;top:126px;width:220px;font-size:9.5px;line-height:12px;color:#fff}
.dot{position:absolute;top:229px;width:9px;height:9px;border-radius:50%;border:1.5px solid #fff}
.dot.on{background:#fff}

/* listing */
.section-title{position:absolute;font-size:10.5px;color:var(--accent);text-transform:uppercase}
.sort-label{left:255px;top:407px;font-size:10.5px;position:absolute}
.sort-btn{position:absolute;top:404px;height:16px;font-size:10px;display:flex;align-items:center;justify-content:center;background:#e4e4e4;color:#333;border:1px solid #ccc}
.sort-btn.active{background:#1c1c1c;color:#fff;border-color:#1c1c1c}
.divider{position:absolute;left:691px;top:404px;width:1px;height:668px;background:var(--line)}

.event-grid{position:absolute;left:147px;top:445px;display:grid;grid-template-columns:repeat(3,161px);column-gap:21px;row-gap:28px}
.event-card{width:161px;height:133px;position:relative}
.event-img{width:161px;height:70px}
.event-title{font-size:12px;color:var(--accent);margin-top:7px}
.event-meta{display:flex;justify-content:space-between;font-size:8.5px;margin-top:5px}
.event-actions{position:absolute;top:114px;left:0;display:flex;gap:4px}
.act{height:20px;font-size:9.5px;color:#fff;display:flex;align-items:center;justify-content:center}
.act-view{width:52px;background:#1f1f1f}
.act-fav{width:105px;background:var(--cta)}

/* sidebar */
.fav-img{position:absolute;left:706px;width:129px;height:70px}
.btn-favs{left:706px;top:689px;width:86px;height:20px;background:#1f1f1f;font-size:9px}
.newsletter-text{position:absolute;left:706px;top:753px;width:135px;font-size:9.5px;line-height:12px;color:var(--muted)}
.email{position:absolute;left:706px;top:817px;width:129px;height:25px;border:1px solid var(--line);font-size:9.5px;color:#999;padding:6px 7px}
.btn-submit{left:706px;top:851px;width:45px;height:20px;background:#1f1f1f;font-size:9.5px}

.pager{position:absolute;left:469px;top:1091px;font-size:10px}
.pager .cur{color:var(--accent)}

/* footer */
.site-footer{position:absolute;left:0;top:1126px;width:983px;height:74px;background:var(--brand);color:#fff}
.footer-links{position:absolute;left:147px;top:21px;font-size:9.5px;white-space:nowrap}
.footer-links span{margin:0 6px}
.copyright{position:absolute;left:148px;top:41px;font-size:9.5px}
</style>
</head>
<body>

<header class="site-header">
  <div class="brand"><div class="brand-name">KULTRO</div><div class="brand-tag">Din Guide til kultur og events</div></div>
  <div class="search">
    <svg width="11" height="11" viewBox="0 0 11 11"><circle cx="4.5" cy="4.5" r="3.5" fill="none" stroke="#999" stroke-width="1.3"/><line x1="7" y1="7" x2="10" y2="10" stroke="#999" stroke-width="1.3"/></svg>Search
  </div>
  <div class="btn-dark btn-search">SOG</div>
  <div class="btn-dark btn-advanced">Avanceret Sogning</div>
  <div class="btn-dark btn-login">Login/Signup</div>
</header>

<nav class="category-nav">
  <ul><li class="active">ALL</li><li>MUSIC</li><li>SPORT</li><li>TEATER</li><li>UPCOMING</li><li>OLDER</li><li>BORN</li><li>MOTION</li><li>DIVERSE</li></ul>
</nav>

<section class="hero" role="img" aria-label="Photo of an elegant couple against a golden sunset sky">
  <div class="hero-title">Upcoming Evetns</div>
  <p class="hero-text">Sed ut perspiciatis unde omnis iste natus error sit voluptatem accusantium doloremque laudantium, totam rem aperiam,</p>
  <span class="dot" style="left:308px"></span><span class="dot on" style="left:337px"></span><span class="dot" style="left:371px"></span>
</section>

<div class="section-title" style="left:147px;top:407px">Popular events</div>
<div class="sort-label">Sorter After</div>
<div class="sort-btn active" style="left:315px;width:52px">Popular</div>
<div class="sort-btn" style="left:373px;width:29px">
  <svg width="18" height="7" viewBox="0 0 18 7"><g fill="#555"><rect x="0" y="0" width="2" height="2"/><rect x="3" y="0" width="2" height="2"/><rect x="0" y="3" width="2" height="2"/><rect x="3" y="3" width="2" height="2"/><rect x="10" y="0" width="1.5" height="1.5"/><rect x="12.5" y="0" width="5" height="1.5"/><rect x="10" y="3" width="1.5" height="1.5"/><rect x="12.5" y="3" width="5" height="1.5"/></g></svg>
</div>
<div class="sort-btn" style="left:408px;width:43px">Date ▾</div>
<div class="sort-btn" style="left:456px;width:32px">Prize</div>

<div class="divider"></div>

<main class="event-grid">
  <article class="event-card"><div class="event-img" role="img" aria-label="Concert crowd with raised hands in yellow stage light" style="background:linear-gradient(180deg,#f2c21a,#b8440c 60%,#2a1206)"></div><h3 class="event-title">Mikkel Strand Koncert</h3><div class="event-meta"><span>Oplev XXXX......</span><span>20/2/2014</span></div><div class="event-actions"><span class="act act-view">Se Event</span><span class="act act-fav">Tilfoj til mine favoritter</span></div></article>
  <article class="event-card"><div class="event-img" role="img" aria-label="Party guests celebrating under confetti" style="background:linear-gradient(135deg,#3a2a5a,#b04a8a 50%,#d8d0e0)"></div><h3 class="event-title">Mikkel Strand Koncert</h3><div class="event-meta"><span>Oplev XXXX......</span><span>20/2/2014</span></div><div class="event-actions"><span class="act act-view">Se Event</span><span class="act act-fav">Tilfoj til mine favoritter</span></div></article>
  <article class="event-card"><div class="event-img" role="img" aria-label="Colourful harbour houses along a canal" style="background:linear-gradient(180deg,#8ab4e0,#e0a040 50%,#9a5a30)"></div><h3 class="event-title">Mikkel Strand Koncert</h3><div class="event-meta"><span>Oplev XXXX......</span><span>20/2/2014</span></div><div class="event-actions"><span class="act act-view">Se Event</span><span class="act act-fav">Tilfoj til mine favoritter</span></div></article>

  <article class="event-card"><div class="event-img" role="img" aria-label="Women dancing at a night party" style="background:linear-gradient(135deg,#2a1208,#c06030 50%,#3a1a10)"></div><h3 class="event-title">Mikkel Strand Koncert</h3><div class="event-meta"><span>Oplev XXXX......</span><span>20/2/2014</span></div><div class="event-actions"><span class="act act-view">Se Event</span><span class="act act-fav">Tilfoj til mine favoritter</span></div></article>
  <article class="event-card"><div class="event-img" role="img" aria-label="Amusement park with illuminated pagoda at dusk" style="background:linear-gradient(180deg,#2a3a8a,#5a4a9a 50%,#c05020)"></div><h3 class="event-title">Mikkel Strand Koncert</h3><div class="event-meta"><span>Oplev XXXX......</span><span>20/2/2014</span></div><div class="event-actions"><span class="act act-view">Se Event</span><span class="act act-fav">Tilfoj til mine favoritter</span></div></article>
  <article class="event-card"><div class="event-img" role="img" aria-label="Friends singing karaoke together" style="background:linear-gradient(135deg,#6a8ab0,#e0b0a0 50%,#8a5a6a)"></div><h3 class="event-title">Mikkel Strand Koncert</h3><div class="event-meta"><span>Oplev XXXX......</span><span>20/2/2014</span></div><div class="event-actions"><span class="act act-view">Se Event</span><span class="act act-fav">Tilfoj til mine favoritter</span></div></article>

  <article class="event-card"><div class="event-img" role="img" aria-label="City skyline with towers at golden hour" style="background:linear-gradient(180deg,#d8b060,#7a6a4a 50%,#3a3a30)"></div><h3 class="event-title">Mikkel Strand Koncert</h3><div class="event-meta"><span>Oplev XXXX......</span><span>20/2/2014</span></div><div class="event-actions"><span class="act act-view">Se Event</span><span class="act act-fav">Tilfoj til mine favoritter</span></div></article>
  <article class="event-card"><div class="event-img" role="img" aria-label="Women celebrating in red club lights" style="background:linear-gradient(135deg,#8a0a0a,#e02a20 50%,#f0c0a0)"></div><h3 class="event-title">Mikkel Strand Koncert</h3><div class="event-meta"><span>Oplev XXXX......</span><span>20/2/2014</span></div><div class="event-actions"><span class="act act-view">Se Event</span><span class="act act-fav">Tilfoj til mine favoritter</span></div></article>
  <article class="event-card"><div class="event-img" role="img" aria-label="Mountains rising above a fjord village" style="background:linear-gradient(180deg,#3a6ab8,#8aa0b0 50%,#1a4a8a)"></div><h3 class="event-title">Mikkel Strand Koncert</h3><div class="event-meta"><span>Oplev XXXX......</span><span>20/2/2014</span></div><div class="event-actions"><span class="act act-view">Se Event</span><span class="act act-fav">Tilfoj til mine favoritter</span></div></article>

  <article class="event-card"><div class="event-img" role="img" aria-label="DJ mixing at a crowded club night" style="background:linear-gradient(135deg,#c03030,#e0a0a0 50%,#3a2a2a)"></div><h3 class="event-title">Mikkel Strand Koncert</h3><div class="event-meta"><span>Oplev XXXX......</span><span>20/2/2014</span></div><div class="event-actions"><span class="act act-view">Se Event</span><span class="act act-fav">Tilfoj til mine favoritter</span></div></article>
  <article class="event-card"><div class="event-img" role="img" aria-label="Lighthouse tower beside a yellow manor under blue sky" style="background:linear-gradient(180deg,#4a7ad0,#a0c0e8 55%,#c0a050)"></div><h3 class="event-title">Mikkel Strand Koncert</h3><div class="event-meta"><span>Oplev XXXX......</span><span>20/2/2014</span></div><div class="event-actions"><span class="act act-view">Se Event</span><span class="act act-fav">Tilfoj til mine favoritter</span></div></article>
  <article class="event-card"><div class="event-img" role="img" aria-label="Hot air balloon over rocky valley" style="background:linear-gradient(180deg,#5a9ad8,#b0d0e8 55%,#8a7a60)"></div><h3 class="event-title">Mikkel Strand Koncert</h3><div class="event-meta"><span>Oplev XXXX......</span><span>20/2/2014</span></div><div class="event-actions"><span class="act act-view">Se Event</span><span class="act act-fav">Tilfoj til mine favoritter</span></div></article>
</main>

<aside>
  <div class="section-title" style="left:706px;top:407px">Mine favoritter</div>
  <div class="fav-img" style="top:445px;background:linear-gradient(180deg,#e8e8e8,#d8a040 50%,#7a7a70)" role="img" aria-label="Old street with yellow houses"></div>
  <div class="fav-img" style="top:526px;background:linear-gradient(180deg,#7aa0c8,#c0c8c0 45%,#8a4a2a)" role="img" aria-label="Historic timber church under evening sky"></div>
  <div class="fav-img" style="top:607px;background:linear-gradient(180deg,#5a90d8,#a8c8e8 50%,#3a5a4a)" role="img" aria-label="Castle towers and statue against blue sky"></div>
  <div class="btn-dark btn-favs">Se mine Favoritter</div>
  <div class="section-title" style="left:705px;top:727px;font-size:13px">Nyhedsbrev</div>
  <p class="newsletter-text">Neque porro quisquam est qui dolorem ipsum quia dolor sit amet, consectetur, adipisci velit...</p>
  <div class="email">Email Address</div>
  <div class="btn-dark btn-submit">Submit</div>
</aside>

<div class="pager"><span class="cur">1</span> &nbsp;|&nbsp; 2 &nbsp;|&nbsp; 3</div>

<footer class="site-footer">
  <div class="footer-links">Om Kultro<span>|</span>Vilkar &amp; betingelser<span>|</span>Kobspolitik<span>|</span>Nyhedsbrev<span>|</span>Kontakt<span>|</span>Login/Register<span>|</span>Hjaelp<span>|</span>For Arrangorer<span>|</span>For Kommuner og Turistforeninger</div>
  <div class="copyright">Copyright © 2014 KULTRO. All rights reserved.</div>
</footer>

</body>
</html>
```